Anselm business card

Business card for commercial photography , photographer specialized in advertising, architecture and interior photography, adventure imagery and camera work. 40 years old, worked for the last 20 years. Business card needs to convey a sense of confidence in work achieved. Card needs to be eye catching as will be left behind in many people's offices. Should also mention discreetly NLVG accredited photographer at the verso of the card. Phone number and website link must be apparent easily.

Target Market(s)

Advertising agencies, commercial photography representation

Industry/Entity Type

Architecture

Contact Information for Business Card

Phone number : +61 470 918 264
anselm.varnet@mailbrook.net
www.anselmvarnet.net

Font styles to use
Sans Serif

Requirements
Must have
• Email adress
• Website
• Phone number
• Name
• Photographer
Nice to have
• NLVG accredited photographer
Should not have
• Rond corners

```html
<!DOCTYPE html>
<html lang="en">
<head>
<meta charset="utf-8">
<title>Anselm Varnet — Business Card</title>
<link href="https://fonts.googleapis.com/css2?family=Questrial&display=swap" rel="stylesheet">
<style>
  :root {
    --stage: #2b2a2a;
    --card-yellow: #fff200;
    --ink-dark: #3a3a3c;
    --icon-box: #3d3d40;
    --white: #ffffff;
    --collage-dark: #1c1a19;
    --collage-mid: #5a5550;
    --collage-light: #8f8a84;
    --band: rgba(20, 16, 14, 0.82);
  }
  * { box-sizing: border-box; margin: 0; padding: 0; }
  html, body {
    width: 1200px; height: 1200px; overflow: hidden;
    background: var(--stage);
    font-family: "Questrial", "Helvetica Neue", Arial, sans-serif;
  }
  .canvas {
    position: relative; width: 1200px; height: 1200px;
    display: flex; flex-direction: column; align-items: center; justify-content: center;
    gap: 56px;
  }
  .card {
    position: relative; width: 900px; height: 514px; overflow: hidden;
    box-shadow: 0 10px 30px rgba(0,0,0,0.45);
  }

  /* Back side: contact details */
  .card--back { background: var(--card-yellow); color: var(--ink-dark); }
  .contact-list {
    position: absolute; left: 0; top: 62px; list-style: none;
    display: flex; flex-direction: column; gap: 10px;
  }
  .contact-item { display: flex; align-items: center; gap: 14px; font-size: 21px; letter-spacing: 0.3px; }
  .contact-icon {
    width: 44px; height: 40px; background: var(--icon-box);
    display: flex; align-items: center; justify-content: center;
  }
  .contact-icon svg { width: 26px; height: 26px; fill: none; stroke: var(--white); stroke-width: 1.6; stroke-linecap: round; stroke-linejoin: round; }
  .back-identity { position: absolute; left: 300px; top: 258px; text-align: right; }
  .back-identity .name { font-size: 50px; letter-spacing: 2px; color: var(--ink-dark); line-height: 1; }
  .back-identity .role { font-size: 21px; letter-spacing: 2px; color: var(--white); margin-top: 2px; }
  .accreditation {
    position: absolute; right: 44px; bottom: 36px;
    font-size: 58px; color: var(--white); letter-spacing: 1px; line-height: 1;
  }

  /* Front side: portfolio collage */
  .card--front { background: var(--collage-dark); }
  .portfolio-collage {
    position: absolute; inset: 0;
    background: radial-gradient(ellipse at 40% 45%, var(--collage-light) 0%, var(--collage-mid) 40%, var(--collage-dark) 100%);
  }
  .name-band {
    position: absolute; left: 170px; top: 205px; width: 520px; height: 118px;
    background: var(--band); padding: 18px 26px 0 26px; text-align: right;
  }
  .name-band .name { font-size: 50px; color: var(--white); letter-spacing: 2px; line-height: 1; text-align: left; white-space: nowrap; }
  .name-band .role { font-size: 24px; color: var(--card-yellow); letter-spacing: 2px; margin-top: 8px; }
</style>
</head>
<body>
<main class="canvas">
  <section class="card card--back" aria-label="Card back: contact details">
    <ul class="contact-list">
      <li class="contact-item">
        <span class="contact-icon"><svg viewBox="0 0 24 24"><path d="M5 3h4l2 5-2.5 1.5a11 11 0 0 0 6 6L16 13l5 2v4a2 2 0 0 1-2 2A17 17 0 0 1 3 5a2 2 0 0 1 2-2z"/></svg></span>
        <span>+61 470 918 264</span>
      </li>
      <li class="contact-item">
        <span class="contact-icon"><svg viewBox="0 0 24 24"><rect x="3" y="6" width="18" height="12"/><path d="M3 6l9 7 9-7"/></svg></span>
        <span>anselm.varnet@mailbrook.net</span>
      </li>
      <li class="contact-item">
        <span class="contact-icon"><svg viewBox="0 0 24 24"><circle cx="12" cy="12" r="9"/><path d="M3 12h18M12 3c3 3 3 15 0 18M12 3c-3 3-3 15 0 18"/></svg></span>
        <span>www.anselmvarnet.net</span>
      </li>
    </ul>
    <div class="back-identity">
      <p class="name">ANSELM VARNET</p>
      <p class="role">PHOTOGRAPHER</p>
    </div>
    <p class="accreditation">nlvg</p>
  </section>

  <section class="card card--front" aria-label="Card front: name over portfolio">
    <div class="portfolio-collage" role="img" aria-label="Grid of black-and-white portfolio photographs: portraits, interiors, landscapes and wildlife"></div>
    <div class="name-band">
      <p class="name">ANSELM VARNET</p>
      <p class="role">PHOTOGRAPHER</p>
    </div>
  </section>
</main>
</body>
</html>
```